Heart Rate Game Display Graphic

We need a unique layout / info-graphic for our heart rate software to display an individuals hear rate, HR%, and other data together within a larger class of up to 40 other users. Graphics should be colorful, dynamic, and intuitive.

Target Market(s)

Group Fitness Classes

Font styles to use
Sans Serif

Colors

Designer to choose colors to be used in the design.

Requirements
Must have
• Individual Box must contain data field or graphic representation of:
• User Name
• Heart Rate %
• Points Earned / % Accuracy
Nice to have
• thinking other shape design that easily integrates with 40+ of the same shape. Looking for depth of design and or some 3d visualizations. Competing companies:
• https://www.pulsevane.org/
• https://www.trovo.com/
• https://www.kestra.com/us-en/club
• https://bravulo.com/
• https://dornaly.fit/personal-trainer/
• https://www.quelvanta.io/Solutions/Heart-Rate-Training
• http://wamble.corvinladesystems.com/
• https://pell-tander.com/explore/pell-tander-indoor-cycling-app/
Should not have
• should NOT be just be plain squares representing each client.

```html
<!DOCTYPE html>
<html lang="en">
<head>
<meta charset="utf-8">
<title>Heart Rate Class Board</title>
<link href="https://fonts.googleapis.com/css2?family=Dosis:wght@300;400&family=Nunito+Sans:wght@700;800;900&display=swap" rel="stylesheet">
<style>
:root{
  --red-a:#e8394f;--red-b:#fb5b69;
  --teal-a:#12b3ab;--teal-b:#2ccbc0;
  --green-a:#1fbe62;--green-b:#2bdc79;
  --purple-a:#8a4fdc;--purple-b:#a561f1;
  --slate-a:#4e5f77;--slate-b:#76859b;
  --orange-a:#fb7d29;--orange-b:#ff9b40;
  --blue-a:#3966df;--blue-b:#5084f2;
  --sky-a:#2d99e5;--sky-b:#49aff3;
  --dark-top:#2c3d5c;--dark-bottom:#34476b;
  --light-top:#f5f7fb;--light-bottom:#e3e8f1;
  --ink:#2a3447;
  --white:#ffffff;
}
*{margin:0;padding:0;box-sizing:border-box}
html,body{width:783px;height:1200px;overflow:hidden;background:var(--light-bottom)}
.stage{width:1200px;height:1838px;transform:scale(.6525);transform-origin:0 0;position:relative}
.panel{position:absolute;left:0;width:1200px;height:919px}
.panel--dark{top:0;background:linear-gradient(var(--dark-top),var(--dark-bottom))}
.panel--light{top:919px;background:linear-gradient(var(--light-top),var(--light-bottom))}
.board{position:absolute;left:46px;top:41px;display:grid;grid-template-columns:repeat(4,247px);column-gap:36px;row-gap:41px}
.card{position:relative;height:150px;border-radius:14px;overflow:hidden;display:grid;grid-template-columns:124px 1fr;color:var(--white);font-family:"Nunito Sans",sans-serif;
  background:linear-gradient(90deg,var(--a) 0 124px,var(--b) 124px)}
.panel--light .card{box-shadow:0 10px 24px -6px color-mix(in srgb,var(--b) 55%,transparent)}
.panel--dark .card{box-shadow:0 8px 18px rgba(10,20,40,.35)}
.card--red{--a:var(--red-a);--b:var(--red-b)}
.card--teal{--a:var(--teal-a);--b:var(--teal-b)}
.card--green{--a:var(--green-a);--b:var(--green-b)}
.card--purple{--a:var(--purple-a);--b:var(--purple-b)}
.card--slate{--a:var(--slate-a);--b:var(--slate-b)}
.card--orange{--a:var(--orange-a);--b:var(--orange-b)}
.card--blue{--a:var(--blue-a);--b:var(--blue-b)}
.card--sky{--a:var(--sky-a);--b:var(--sky-b)}
.card__name{position:absolute;top:0;left:32px;width:184px;height:31px;background:var(--white);border-radius:0 0 16px 16px;color:var(--ink);font-weight:800;font-size:16px;text-align:center;line-height:33px}
.card__hr,.card__score{display:flex;flex-direction:column;align-items:center;padding-top:46px}
.card__hr b{font-family:"Dosis",sans-serif;font-weight:300;font-size:66px;line-height:58px;letter-spacing:-1px}
.card__hr span{font-weight:800;font-size:14px;margin-top:6px}
.card__score b{font-family:"Dosis",sans-serif;font-weight:300;font-size:34px;line-height:40px;margin-top:4px}
.card__score span{font-weight:800;font-size:11.5px;line-height:14px;text-align:center;margin-top:10px}
.bar{position:absolute;left:41px;top:809px;width:1103px;height:71px;background:var(--white);border-radius:16px;box-shadow:0 8px 20px rgba(20,30,60,.15)}
.bar__dots{position:absolute;left:23px;top:26px;display:flex;gap:26px}
.bar__dots i{width:20px;height:20px;border-radius:50%;background:var(--c)}
.timer{position:absolute;left:410px;top:10px;width:284px;height:51px;border-radius:12px;background:linear-gradient(90deg,var(--red-a),var(--red-b));color:var(--white);font-family:"Nunito Sans",sans-serif}
.timer__label{position:absolute;left:18px;top:18px;font-size:11px;font-weight:800}
.timer__value{position:absolute;right:24px;top:-2px;font-family:"Dosis",sans-serif;font-weight:300;font-size:50px;line-height:56px}
.brand{position:absolute;right:28px;top:22px;font-family:"Nunito Sans",sans-serif;font-weight:800;font-size:22px;color:var(--ink)}
</style>
</head>
<body>
<div class="stage">

<section class="panel panel--dark">
  <div class="board">
    <div class="card card--red"><div class="card__name">Marisol T.21</div><div class="card__hr"><b>170</b><span>HEART RATE</span></div><div class="card__score"><b>36/91%</b><span>POINTS &amp;<br>ACCURACY</span></div></div>
    <div class="card card--teal"><div class="card__name">Joanna P.24</div><div class="card__hr"><b>189</b><span>HEART RATE</span></div><div class="card__score"><b>15/93%</b><span>POINTS &amp;<br>ACCURACY</span></div></div>
    <div class="card card--green"><div class="card__name">Lorena B.5</div><div class="card__hr"><b>175</b><span>HEART RATE</span></div><div class="card__score"><b>10/90%</b><span>POINTS &amp;<br>ACCURACY</span></div></div>
    <div class="card card--purple"><div class="card__name">Hazel R.20</div><div class="card__hr"><b>155</b><span>HEART RATE</span></div><div class="card__score"><b>6/87%</b><span>POINTS &amp;<br>ACCURACY</span></div></div>
    <div class="card card--slate"><div class="card__name">Hazel W.26</div><div class="card__hr"><b>183</b><span>HEART RATE</span></div><div class="card__score"><b>16/89%</b><span>POINTS &amp;<br>ACCURACY</span></div></div>
    <div class="card card--orange"><div class="card__name">Danielle F.13</div><div class="card__hr"><b>190</b><span>HEART RATE</span></div><div class="card__score"><b>9/93%</b><span>POINTS &amp;<br>ACCURACY</span></div></div>
    <div class="card card--blue"><div class="card__name">Owen D.19</div><div class="card__hr"><b>158</b><span>HEART RATE</span></div><div class="card__score"><b>13/90%</b><span>POINTS &amp;<br>ACCURACY</span></div></div>
    <div class="card card--sky"><div class="card__name">Skylark</div><div class="card__hr"><b>191</b><span>HEART RATE</span></div><div class="card__score"><b>15/96%</b><span>POINTS &amp;<br>ACCURACY</span></div></div>
    <div class="card card--purple"><div class="card__name">Wendy H.20</div><div class="card__hr"><b>180</b><span>HEART RATE</span></div><div class="card__score"><b>18/101%</b><span>POINTS &amp;<br>ACCURACY</span></div></div>
    <div class="card card--red"><div class="card__name">Iris P.3</div><div class="card__hr"><b>173</b><span>HEART RATE</span></div><div class="card__score"><b>13/96%</b><span>POINTS &amp;<br>ACCURACY</span></div></div>
    <div class="card card--slate"><div class="card__name">Selma Q.6</div><div class="card__hr"><b>160</b><span>HEART RATE</span></div><div class="card__score"><b>7/90%</b><span>POINTS &amp;<br>ACCURACY</span></div></div>
    <div class="card card--green"><div class="card__name">Perry N.6</div><div class="card__hr"><b>180</b><span>HEART RATE</span></div><div class="card__score"><b>13/95%</b><span>POINTS &amp;<br>ACCURACY</span></div></div>
    <div class="card card--sky"><div class="card__name">Aaron B.22</div><div class="card__hr"><b>153</b><span>HEART RATE</span></div><div class="card__score"><b>13/88%</b><span>POINTS &amp;<br>ACCURACY</span></div></div>
    <div class="card card--orange"><div class="card__name">Oscar T.32</div><div class="card__hr"><b>158</b><span>HEART RATE</span></div><div class="card__score"><b>13/92%</b><span>POINTS &amp;<br>ACCURACY</span></div></div>
    <div class="card card--purple"><div class="card__name">Renzo K.6</div><div class="card__hr"><b>142</b><span>HEART RATE</span></div><div class="card__score"><b>6/72%</b><span>POINTS &amp;<br>ACCURACY</span></div></div>
    <div class="card card--blue"><div class="card__name">Clara E.5</div><div class="card__hr"><b>180</b><span>HEART RATE</span></div><div class="card__score"><b>8/88%</b><span>POINTS &amp;<br>ACCURACY</span></div></div>
  </div>
  <div class="bar">
    <div class="bar__dots"><i style="--c:var(--teal-a)"></i><i style="--c:var(--orange-a)"></i><i style="--c:var(--purple-a)"></i><i style="--c:var(--red-a)"></i><i style="--c:var(--green-a)"></i></div>
    <div class="timer"><span class="timer__label">TIME</span><span class="timer__value">00:00.30</span></div>
    <div class="brand">YOURLOGO</div>
  </div>
</section>

<section class="panel panel--light">
  <div class="board">
    <div class="card card--red"><div class="card__name">Marisol T.21</div><div class="card__hr"><b>170</b><span>HEART RATE</span></div><div class="card__score"><b>36/91%</b><span>POINTS &amp;<br>ACCURACY</span></div></div>
    <div class="card card--teal"><div class="card__name">Joanna P.24</div><div class="card__hr"><b>189</b><span>HEART RATE</span></div><div class="card__score"><b>15/93%</b><span>POINTS &amp;<br>ACCURACY</span></div></div>
    <div class="card card--green"><div class="card__name">Lorena B.5</div><div class="card__hr"><b>175</b><span>HEART RATE</span></div><div class="card__score"><b>10/90%</b><span>POINTS &amp;<br>ACCURACY</span></div></div>
    <div class="card card--purple"><div class="card__name">Hazel R.20</div><div class="card__hr"><b>155</b><span>HEART RATE</span></div><div class="card__score"><b>6/87%</b><span>POINTS &amp;<br>ACCURACY</span></div></div>
    <div class="card card--slate"><div class="card__name">Hazel W.26</div><div class="card__hr"><b>183</b><span>HEART RATE</span></div><div class="card__score"><b>16/89%</b><span>POINTS &amp;<br>ACCURACY</span></div></div>
    <div class="card card--orange"><div class="card__name">Danielle F.13</div><div class="card__hr"><b>190</b><span>HEART RATE</span></div><div class="card__score"><b>9/93%</b><span>POINTS &amp;<br>ACCURACY</span></div></div>
    <div class="card card--blue"><div class="card__name">Owen D.19</div><div class="card__hr"><b>158</b><span>HEART RATE</span></div><div class="card__score"><b>13/90%</b><span>POINTS &amp;<br>ACCURACY</span></div></div>
    <div class="card card--sky"><div class="card__name">Skylark</div><div class="card__hr"><b>191</b><span>HEART RATE</span></div><div class="card__score"><b>15/96%</b><span>POINTS &amp;<br>ACCURACY</span></div></div>
    <div class="card card--purple"><div class="card__name">Wendy H.20</div><div class="card__hr"><b>180</b><span>HEART RATE</span></div><div class="card__score"><b>18/101%</b><span>POINTS &amp;<br>ACCURACY</span></div></div>
    <div class="card card--red"><div class="card__name">Iris P.3</div><div class="card__hr"><b>173</b><span>HEART RATE</span></div><div class="card__score"><b>13/96%</b><span>POINTS &amp;<br>ACCURACY</span></div></div>
    <div class="card card--slate"><div class="card__name">Selma Q.6</div><div class="card__hr"><b>160</b><span>HEART RATE</span></div><div class="card__score"><b>7/90%</b><span>POINTS &amp;<br>ACCURACY</span></div></div>
    <div class="card card--green"><div class="card__name">Perry N.6</div><div class="card__hr"><b>180</b><span>HEART RATE</span></div><div class="card__score"><b>13/95%</b><span>POINTS &amp;<br>ACCURACY</span></div></div>
    <div class="card card--sky"><div class="card__name">Aaron B.22</div><div class="card__hr"><b>153</b><span>HEART RATE</span></div><div class="card__score"><b>13/88%</b><span>POINTS &amp;<br>ACCURACY</span></div></div>
    <div class="card card--orange"><div class="card__name">Oscar T.32</div><div class="card__hr"><b>158</b><span>HEART RATE</span></div><div class="card__score"><b>13/92%</b><span>POINTS &amp;<br>ACCURACY</span></div></div>
    <div class="card card--purple"><div class="card__name">Renzo K.6</div><div class="card__hr"><b>142</b><span>HEART RATE</span></div><div class="card__score"><b>6/72%</b><span>POINTS &amp;<br>ACCURACY</span></div></div>
    <div class="card card--blue"><div class="card__name">Clara E.5</div><div class="card__hr"><b>180</b><span>HEART RATE</span></div><div class="card__score"><b>8/88%</b><span>POINTS &amp;<br>ACCURACY</span></div></div>
  </div>
  <div class="bar">
    <div class="bar__dots"><i style="--c:var(--teal-a)"></i><i style="--c:var(--orange-a)"></i><i style="--c:var(--purple-a)"></i><i style="--c:var(--red-a)"></i><i style="--c:var(--green-a)"></i></div>
    <div class="timer"><span class="timer__label">TIME</span><span class="timer__value">00:00.30</span></div>
    <div class="brand">YOURLOGO</div>
  </div>
</section>

</div>
</body>
</html>
```